YARD CRAFTERS "N" CO

catyering to driveway/patio floor construction and remodeling. Concrete, concrete pavers, asphalt, Landscaping, irrigation, pergolas and pools.

Target Market(s)

the home owner that wants to enhance their home

Industry/Entity Type

construction

Contact Information for Business Card

presidet: lino barrega email: yardcraftersnco@mailbox.test office/cell: 555 204 8813

Font styles to use
Sans Serif

Requirements
Must have
• logo should pop out
Nice to have
• the logo should demonstrate that we do exteriors only

```html
<!DOCTYPE html>
<html lang="en">
<head>
<meta charset="utf-8">
<title>Yard Crafters "N" Co – Business Card</title>
<link rel="stylesheet" href="https://fonts.googleapis.com/css2?family=Open+Sans:wght@400;600;700;800&display=swap">
<style>
  :root {
    --backdrop: #242424;
    --card: #222126;
    --edge: #e3151e;
    --red: #ec1c24;
    --grey: #a3a3a6;
    --white: #ffffff;
  }
  * { margin: 0; padding: 0; box-sizing: border-box; }
  html, body {
    width: 1200px; height: 780px; overflow: hidden;
    background: var(--backdrop);
    font-family: "Open Sans", Arial, sans-serif;
  }
  .stage {
    position: relative; width: 1200px; height: 780px;
  }
  .card {
    position: absolute; top: 48px;
    width: 390px; height: 684px;
    background: var(--card);
    border-radius: 30px;
    box-shadow: 0 4px 0 var(--edge), 0 18px 30px rgba(0,0,0,.55);
    overflow: hidden;
  }
  .card--front { left: 170px; }
  .card--back { left: 640px; color: var(--white); text-align: center; }

  /* front: vertical wordmark */
  .front-mark {
    position: absolute; left: 50%; top: 50%;
    transform: translate(-50%, -50%) rotate(90deg);
    display: flex; align-items: center; gap: 18px;
    white-space: nowrap;
  }
  .mark-square { width: 34px; height: 34px; background: var(--red); }
  .front-mark .mark-name {
    font-weight: 800; font-size: 58px; letter-spacing: 1px;
    color: var(--grey); text-transform: uppercase;
  }

  /* back */
  .back-mark {
    position: absolute; top: 92px; left: 0; right: 0;
    display: flex; justify-content: center; align-items: center; gap: 10px;
  }
  .back-mark .mark-square { width: 16px; height: 16px; }
  .back-mark .mark-name {
    font-weight: 800; font-size: 28px; color: var(--grey); text-transform: uppercase;
  }
  .holder { position: absolute; top: 268px; left: 0; right: 0; }
  .holder-name { font-size: 36px; font-weight: 800; line-height: 1; }
  .holder-name .first { color: var(--red); }
  .holder-name .last { color: var(--grey); }
  .holder-role { font-size: 17px; font-weight: 700; margin-top: 6px; }

  .dot-row { position: absolute; left: 0; width: 390px; height: 30px; }
  .dot-row--contact { top: 344px; }
  .dot-row--services { top: 460px; }

  .contact { position: absolute; top: 384px; left: 0; right: 0; }
  .contact-phone { font-size: 32px; font-weight: 800; line-height: 1.1; }
  .contact-email { font-size: 15.5px; font-weight: 600; margin-top: 4px; }

  .services-pill {
    position: absolute; top: 459px; left: 50%; transform: translateX(-50%);
    background: var(--red); color: var(--white);
    font-weight: 800; font-size: 16px; letter-spacing: .5px;
    padding: 4px 18px; border-radius: 20px;
  }
  .services-list {
    position: absolute; top: 500px; left: 0; right: 0;
    list-style: none; font-size: 15px; font-weight: 600; line-height: 1.42;
  }
</style>
</head>
<body>
<main class="stage">

  <section class="card card--front" aria-label="Card front">
    <div class="front-mark">
      <span class="mark-square"></span>
      <span class="mark-name">Lino Barrega</span>
    </div>
  </section>

  <section class="card card--back" aria-label="Card back">
    <div class="back-mark">
      <span class="mark-square"></span>
      <span class="mark-name">Lino Barrega</span>
    </div>

    <div class="holder">
      <h1 class="holder-name"><span class="first">Lino</span> <span class="last">Barrega</span></h1>
      <p class="holder-role">Presidet</p>
    </div>

    <svg class="dot-row dot-row--contact" viewBox="0 0 390 30" aria-hidden="true">
      <g fill="#ec1c24">
        <circle cx="14" cy="15" r="3"/><circle cx="32" cy="15" r="4"/><circle cx="52" cy="15" r="5"/>
        <circle cx="74" cy="15" r="6.5"/><circle cx="100" cy="15" r="8"/><circle cx="128" cy="15" r="9"/>
        <circle cx="172" cy="15" r="12"/><circle cx="218" cy="15" r="12"/>
        <circle cx="262" cy="15" r="9"/><circle cx="290" cy="15" r="8"/><circle cx="316" cy="15" r="6.5"/>
        <circle cx="338" cy="15" r="5"/><circle cx="358" cy="15" r="4"/><circle cx="376" cy="15" r="3"/>
      </g>
      <path d="M167 10c1-1 2-1 3 1l1 2c0 1-1 1-1 2 1 2 2 3 4 4 1 0 1-1 2-1l2 1c2 1 2 2 1 3-1 2-3 2-5 1-3-1-6-4-7-7-1-2-1-4 0-6z" fill="#fff"/>
      <rect x="211" y="10" width="14" height="10" rx="1" fill="none" stroke="#fff" stroke-width="1.6"/>
      <path d="M211 10l7 6 7-6" fill="none" stroke="#fff" stroke-width="1.6"/>
    </svg>

    <div class="contact">
      <p class="contact-phone">555 204 8813</p>
      <p class="contact-email">yardcraftersnco@mailbox.test</p>
    </div>

    <svg class="dot-row dot-row--services" viewBox="0 0 390 30" aria-hidden="true">
      <g fill="#ec1c24">
        <circle cx="14" cy="15" r="3"/><circle cx="30" cy="15" r="3.5"/><circle cx="48" cy="15" r="4.5"/>
        <circle cx="68" cy="15" r="5.5"/><circle cx="90" cy="15" r="6.5"/><circle cx="114" cy="15" r="7.5"/>
        <circle cx="276" cy="15" r="7.5"/><circle cx="300" cy="15" r="6.5"/><circle cx="322" cy="15" r="5.5"/>
        <circle cx="342" cy="15" r="4.5"/><circle cx="360" cy="15" r="3.5"/><circle cx="376" cy="15" r="3"/>
      </g>
    </svg>
    <span class="services-pill">SERVICES</span>

    <ul class="services-list">
      <li>Asphalt</li>
      <li>Irrigation</li>
      <li>Concrete</li>
      <li>Landscaping</li>
      <li>Concrete pavers</li>
      <li>Pergolas and pools</li>
      <li>Catyering to driveway</li>
      <li>Patio floor construction and remodeling</li>
    </ul>
  </section>

</main>
</body>
</html>
```